Martin Hale PA Card Logo

Current logo attached. Its 25 year old logo I have used. Looking for a new fresh elegant professional look/design for a law firm that has high net worth clientele and is estate planning business law firm. Firm mis in Palm Beach Florida.
One sided card linen stock white will be used. Logo section name section. Logo should include nice elegant design using the letter "M" perhapa (I am not wed to current font of the M on current logo.) Be creative there with logo design. My initials are MH.......color scheme I figure 3 tone... Raised Gold Foil, Blue name of firm = Martin Hale, P.A. My practice focus is Family and Business Asset Protection. My name is Martin M. Hale, Esq. Practice specialties include Asset Protection trusts, Business Succession Planning, LLC law, Estate Planning, Medicaid Planning (Maybe put those topics in bullets in a section of card. Bottom of card can be reserved smaller print address phone website and email address. Address section is not as important as logo and topics of practice on front. I foresee address section can be in dark blue. MY name and Topics dark blue as well.
Target Market(s)
affluent; business owners executives; wealth 2-10 million net worth
Industry/Entity Type
business law and estate planning
Contact Information for Business Card
White thick linen one sided

```html
<!DOCTYPE html>
<html lang="en">
<head>
<meta charset="utf-8">
<title>Martin Hale, P.A. — Business Card</title>
<link rel="stylesheet" href="https://fonts.googleapis.com/css2?family=Cinzel:wght@400;600&family=Poppins:wght@300;400&display=swap">
<style>
  :root {
    --navy: #1f2f4b;
    --navy-deep: #15223a;
    --copper: #b8652a;
    --ink: #3a3f4a;
    --card: #f4f5f7;
    --backdrop: #e4e2de;
  }
  * { margin: 0; padding: 0; box-sizing: border-box; }
  html, body {
    width: 1200px; height: 970px; overflow: hidden;
    background: var(--backdrop);
  }
  .card {
    position: absolute; left: 50px; top: 170px;
    width: 1100px; height: 629px;
    background: linear-gradient(135deg, #ffffff 0%, var(--card) 55%, #ecebea 100%);
    overflow: hidden;
    box-shadow: 0 10px 30px rgba(0,0,0,.18);
  }
  .card__ornament { position: absolute; inset: 0; width: 100%; height: 100%; }
  .firm {
    position: absolute; left: 530px; top: 66px; width: 520px;
    text-align: center; color: var(--navy);
    font-family: "Cinzel", serif;
  }
  .firm__mark {
    display: block; width: 54px; height: 54px; margin: 0 auto 34px;
    border-radius: 50%; background: var(--copper);
  }
  .firm__name { font-size: 48px; font-weight: 600; letter-spacing: 2px; line-height: 1; white-space: nowrap; }
  .firm__tagline { margin-top: 14px; font-size: 25px; font-weight: 600; letter-spacing: 5px; line-height: 1; white-space: nowrap; }
  .person { position: absolute; left: 65px; top: 232px; }
  .person__name {
    font-family: "Cinzel", serif; font-size: 38px; font-weight: 400;
    color: var(--navy); letter-spacing: 1px; line-height: 1;
  }
  .person__role {
    margin-top: 10px; font-family: "Poppins", sans-serif; font-size: 25px;
    font-weight: 300; color: var(--copper); line-height: 1.1;
  }
  .address {
    position: absolute; left: 65px; top: 326px;
    font-family: "Poppins", sans-serif; font-size: 24px; font-weight: 300;
    font-style: normal; color: var(--ink); line-height: 33px;
  }
  .contacts {
    position: absolute; left: 65px; top: 417px; list-style: none;
    font-family: "Poppins", sans-serif; font-size: 25px; font-weight: 300;
    color: var(--ink);
  }
  .contacts__item { display: flex; align-items: center; height: 35px; }
  .contacts__icon { width: 28px; height: 28px; margin-right: 14px; flex: none; }
</style>
</head>
<body>
  <main class="card">
    <svg class="card__ornament" viewBox="0 0 1100 629" aria-hidden="true">
      <path d="M0 0 H215 Q90 60 0 118 Z" fill="var(--navy)"/>
      <path d="M215 0 Q90 60 0 118 V128 Q95 66 232 0 Z" fill="var(--copper)"/>
      <path d="M440 0 H500 Q210 95 0 232 V210 Q190 85 440 0 Z" fill="var(--navy)"/>
      <path d="M0 548 Q550 608 1100 540 V629 H0 Z" fill="var(--copper)"/>
      <path d="M0 566 Q550 622 1100 552 V629 H0 Z" fill="var(--navy-deep)"/>
    </svg>

    <header class="firm">
      <span class="firm__mark" role="img" aria-label="Firm monogram"></span>
      <div class="firm__name">Martin Hale, P.A</div>
      <div class="firm__tagline">Elder Law Attorney</div>
    </header>

    <section class="person">
      <div class="person__name">Daniel Reyes</div>
      <div class="person__role">Founder/Director</div>
    </section>

    <address class="address">
      PO Box 418 Harbor Road<br>
      2nd Street Palm Beach
    </address>

    <ul class="contacts">
      <li class="contacts__item">
        <svg class="contacts__icon" viewBox="0 0 28 28" aria-hidden="true">
          <circle cx="14" cy="14" r="14" fill="var(--copper)"/>
          <rect x="9" y="6" width="10" height="16" rx="2" fill="none" stroke="#fff" stroke-width="2"/>
        </svg>(01) 4826 1937
      </li>
      <li class="contacts__item">
        <svg class="contacts__icon" viewBox="0 0 28 28" aria-hidden="true">
          <circle cx="14" cy="14" r="14" fill="var(--copper)"/>
          <path d="M7 12 Q14 6 21 12 L19 14 L16 12 V10 H12 V12 L9 14 Z" fill="#fff"/>
          <rect x="9" y="15" width="10" height="6" rx="1" fill="#fff"/>
        </svg>(01) 4826 1937
      </li>
      <li class="contacts__item">
        <svg class="contacts__icon" viewBox="0 0 28 28" aria-hidden="true">
          <circle cx="14" cy="14" r="14" fill="var(--copper)"/>
          <rect x="7" y="9" width="14" height="10" rx="1" fill="none" stroke="#fff" stroke-width="1.8"/>
          <path d="M7 9 L14 15 L21 9" fill="none" stroke="#fff" stroke-width="1.8"/>
        </svg>info@halelawoffice.com
      </li>
    </ul>
  </main>
</body>
</html>
```